App Store Screenshot Design for Vaccination Record App (iOS)

Project Description
We are looking for a professional graphic designer to redesign our App Store screenshots for our iOS app Medlo, a personal vaccination record app.
The goal is to significantly improve App Store conversion by creating screenshots that look:
• Clean
• Trustworthy
• Modern
• Medical but friendly
• Suitable for parents and older adults
Our current screenshots feel too “developer-like.” We want to match or exceed the visual quality of top competitors in this category.
⸻
About the App
Medlo helps people:
• Store all their vaccinations in one place
• Upload and scan vaccination proofs. Medlo automatically recognizes vaccines from photos, making imports fast and effortless.
• Receive reminders for boosters and expiring vaccinations
• Manage profiles for family members
• Export records (PDF) for school, work, or travel
Target users:
• Parents (tracking children’s vaccinations)
• Adults 45+
• Travelers
• Caregivers
This is not a children’s app — it’s a serious health utility that must feel reliable and credible.
⸻
Target Audience
Primary:
• Parents
• Older adults (45+)
Secondary:
• Travelers
• Caregivers
Design should feel:
• Calm
• Reassuring
• Clear
• Easy to understand at a glance
⸻
What We Need
1. App Store Screenshot Designs
• iPhone and iPad format (Apple App Store guidelines)
• Approx. 5–7 screenshots
• Focus on benefits, not features
• Short, strong headlines
• Clean UI framing
Important:
These screenshots are marketing visuals for the App Store.
They do NOT need to reflect the app UI 1:1.
You may crop, frame, abstract, or stylize the app screens to improve clarity and conversion.
2. Editable Figma File
This is very important.
All text in the screenshots must be:
• Easily editable in Figma
• Not baked into images
• Structured so we can localize into multiple languages (EN, NL, DE, FR, ES)
Think:
• Text layers
• Components
• Smart layout for longer translations
⸻
Style & Visual Direction
We like:
• Clean gradients
• Medlo orange / trustworthy colors
• Real people (optional but preferred)
• Subtle medical cues (e.g. bandage / plaster on arm)
We specifically like the first screenshot of this competitor:
👉 https://apps.quorvane.example/us/app/shotlog-tracker/id4827150396
(The woman with a bandage on her arm works very well.)
We want a similar level of polish, but not a copy.
We strongly encourage designers to explore two visual directions:
• A safe, refined direction closely aligned with the current app UI
• A more conceptual / aspirational direction focused on trust, peace of mind, and emotional reassurance
We are open to combining the best elements of both.
Color guidance:
Medlo’s brand color is orange.
Designs should feel medical and trustworthy, but must remain clearly aligned with our brand.
Avoid switching to generic blue-only medical palettes.
⸻
What We Don’t Want
• Overly playful or childish designs
• Overloaded screens
• Technical / developer-style visuals
• Stock images that feel fake or cheesy
⸻
Deliverables
• App Store screenshot designs (iphone and ipad)
• Fully editable Figma file
• Clear text hierarchy
• Ready for localization
⸻
Success Criteria
Primary goal:
Increase App Store page conversion (install rate).
A successful design:
• Looks immediately trustworthy
• Clearly communicates value in <3 seconds
• Feels competitive with top health apps
• Improves App Store conversion
⸻
References
Our app (current version):
https://apps.quorvane.example/us/app/medlo-vaccination-record/id7381029546
Competitor we admire visually:
https://apps.quorvane.example/us/app/shotlog-tracker/id4827150396
⸻
Extra Context (Optional for Designers)
This app already has:
• 200k users
• Active international expansion
• Paid subscriptions
This is not a hobby project — we are investing in quality.

```html
<!DOCTYPE html>
<html lang="en">
<head>
<meta charset="utf-8">
<title>Medlo – App Store Screens</title>
<link rel="stylesheet" href="https://fonts.googleapis.com/css2?family=Poppins:wght@600;700&family=Inter:wght@400;500;600;700&display=swap">
<style>
:root{
  --bg:#c8c8c8;
  --orange:#f5a81c;
  --amber:#fcc632;
  --glow:#fdd85a;
  --ink:#151515;
  --screen:#f3f3f5;
  --card:#ffffff;
  --line:#e6e6e9;
  --muted:#9b9ba1;
  --soft:#c4c4c9;
  --accent:#f5b51c;
  --blue:#1a6fe0;
  --red:#e4583b;
  --pill:#3a3a3f;
}
*{box-sizing:border-box;margin:0;padding:0}
html,body{width:1200px;height:440px;overflow:hidden;background:var(--bg)}
.canvas{position:relative;width:1200px;height:440px;background:var(--bg);font-family:"Inter",sans-serif;color:var(--ink)}
.shot{position:absolute;top:46px;width:161px;height:349px;border-radius:18px;overflow:hidden;
  background:
   radial-gradient(circle at 88% 4%, rgba(253,216,90,.9) 0 34%, transparent 35%),
   linear-gradient(180deg,var(--orange) 0%,var(--amber) 55%,#f9bd28 100%)}
.headline{position:absolute;top:20px;left:0;right:0;text-align:center;font-family:"Poppins",sans-serif;font-weight:600;font-size:13px;line-height:16px;color:var(--ink);z-index:2;
  text-shadow:1px 0 #fff,-1px 0 #fff,0 1px #fff,0 -1px #fff,1px 1px #fff,-1px -1px #fff,1px -1px #fff,-1px 1px #fff}
.feature-icon{position:absolute;left:50%;top:72px;width:46px;height:46px;transform:translateX(-50%);border-radius:50%;
  background:radial-gradient(circle,var(--glow) 0 55%,rgba(253,216,90,0) 72%);display:flex;align-items:center;justify-content:center}
.feature-icon svg{width:32px;height:32px}
.portrait{position:absolute;left:46px;top:74px;width:70px;height:110px;border-radius:35px 35px 10px 10px;
  background:linear-gradient(180deg,#b8733a 0%,#e2ab80 40%,#f0c9a5 100%)}
.phone{position:absolute;left:17px;top:118px;width:128px;height:270px;background:#111;border-radius:20px;padding:3px}
.phone.small{left:19px;top:173px;width:126px}
.screen{position:relative;height:100%;background:var(--screen);border-radius:17px;overflow:hidden}
.island{position:absolute;top:5px;left:50%;transform:translateX(-50%);width:36px;height:9px;border-radius:6px;background:#111}
.status{display:flex;justify-content:space-between;padding:6px 10px 0;font-size:5px;font-weight:600;height:16px}
.title{font-weight:700;font-size:9px;padding:4px 8px 4px;display:flex;justify-content:space-between;align-items:center}
.title small{font-size:5px;color:var(--muted);font-weight:500}
.tabs{display:flex;gap:3px;padding:2px 8px 5px}
.tab{font-size:4px;padding:2px 5px;border-radius:5px;background:#e4e4e8}
.tab.on{background:var(--pill);color:#fff}
.panel{background:var(--card);margin:0 5px 5px;border-radius:5px;padding:3px 5px}
.label{font-size:4.6px;font-weight:600;display:flex;justify-content:space-between;align-items:center;padding:2px 0}
.dot{width:7px;height:5px;border-radius:3px;background:var(--accent)}
.row{display:flex;justify-content:space-between;align-items:center;padding:3px 0;border-bottom:1px solid var(--line);font-size:4.4px}
.row:last-child{border-bottom:0}
.row b{font-weight:600;display:block}
.row i{font-style:normal;color:var(--muted);font-size:3.6px;display:block;line-height:5px}
.tag{font-size:3.2px;color:var(--red);background:#fde6e1;padding:1px 3px;border-radius:3px}
.chev{color:var(--soft);font-size:6px}
.upload{display:flex;gap:5px;padding:4px 6px;border-bottom:1px solid var(--line);background:var(--card);font-size:4.4px}
.thumb{width:18px;height:22px;border-radius:2px;background:linear-gradient(160deg,#d9d6cf,#9d9891);flex:none}
.upload b{font-weight:600;display:block}
.upload i{font-style:normal;color:var(--muted);font-size:3.6px}
.fab{position:absolute;right:10px;width:13px;height:13px;border-radius:50%;background:var(--accent);color:#fff;font-size:9px;line-height:13px;text-align:center}
.avatar{width:8px;height:8px;border-radius:50%;background:#b9a08c;display:inline-block;margin-right:3px;vertical-align:middle;flex:none}
.person{display:flex;align-items:center}
.mail{position:absolute;left:51px;top:234px;width:61px;height:61px;border-radius:50%;background:var(--blue);display:flex;align-items:center;justify-content:center}
.toast{position:absolute;left:33px;top:324px;width:95px;height:22px;background:#111;border-radius:3px;color:#fff;padding:3px 4px;display:flex;gap:3px;align-items:center}
.toast .bell{width:10px;height:10px;border-radius:3px;background:var(--accent);flex:none}
.toast b{font-size:5.5px;display:block}
.toast i{font-style:normal;font-size:2.6px;opacity:.8;display:block;line-height:3.4px}
.segment{display:flex;font-size:4.4px;color:var(--muted);margin:0 8px 5px;border-bottom:1px solid var(--line)}
.segment span{flex:1;text-align:center;padding:3px 0}
.segment .on{color:var(--ink);border-bottom:1px solid var(--accent)}
.cta{background:var(--blue);color:#fff;font-size:4.4px;text-align:center;border-radius:3px;padding:3px 0;margin:4px 0 2px;font-weight:600}
.flag{width:7px;height:5px;border-radius:1px;background:var(--red);display:inline-block;margin-right:3px;vertical-align:middle}
.toggle{width:13px;height:7px;border-radius:4px;background:var(--accent);position:relative;flex:none}
.toggle::after{content:"";position:absolute;right:1px;top:1px;width:5px;height:5px;border-radius:50%;background:#fff}
.search{background:var(--card);margin:2px 6px 5px;border-radius:4px;padding:4px 6px;font-size:4px;color:var(--muted)}
.grid{display:grid;grid-template-columns:1fr 1fr;gap:3px;padding:0 6px}
.dest{background:var(--card);border-radius:3px;padding:6px 4px;font-size:4.4px}
.more{text-align:center;font-size:3.8px;color:var(--accent);padding:5px 0}
.badge{position:absolute;left:103px;top:320px;width:34px;height:34px;border-radius:50%;background:#fff;border:2px solid var(--ink);display:flex;align-items:center;justify-content:center}
.note{padding:0 8px;font-size:3.6px;color:var(--muted);font-weight:500}
</style>
</head>
<body>
<main class="canvas">

  <section class="shot" style="left:43px">
    <h2 class="headline">All Your<br>Vaccination<br>in One Place</h2>
    <div class="portrait" role="img" aria-label="Photo of a smiling woman with a plaster on her upper arm"></div>
    <div class="phone small"><div class="screen">
      <div class="island"></div>
      <div class="status"><span>14:21</span><span>●●●</span></div>
      <div class="title">My Vaccinations <small>⚙</small></div>
      <div class="tabs"><span class="tab on">Daniel</span><span class="tab">Ruben</span><span class="tab">Noah</span><span class="tab">Ella</span><span class="tab">Mia</span></div>
      <div class="panel">
        <div class="label">Expiring soon <span class="dot"></span></div>
        <div class="row"><span><b>Hepatitis B</b><i>Daniel</i></span><span class="tag">15 days left</span></div>
        <div class="row"><span><b>Corona / Covid-19</b><i>Daniel</i></span><span class="tag">1 month left</span></div>
      </div>
      <div class="panel">
        <div class="row"><span><b>Shingles (Herpes Zoster)</b><i>Brand: Velmora</i><i>Add Date: 2025-11-03</i></span><span class="chev">›</span></div>
        <div class="row"><span><b>Chikungunya</b><i>Last added: 2025-10-17</i><i>Total registrations: 4</i></span><span class="chev">›</span></div>
        <div class="row"><span><b>Meningitis</b><i>Last added: 2025-09-30</i></span><span class="chev">›</span></div>
      </div>
    </div></div>
    <div class="badge"><svg width="18" height="20" viewBox="0 0 18 20"><path d="M9 1 2 4v5c0 5 3 8 7 10 4-2 7-5 7-10V4z" fill="var(--accent)" stroke="#111" stroke-width="1.5"/><rect x="6" y="9" width="6" height="5" fill="#111"/><path d="M7 9V7a2 2 0 0 1 4 0v2" fill="none" stroke="#111" stroke-width="1.2"/></svg></div>
  </section>

  <section class="shot" style="left:234px">
    <h2 class="headline">Upload Your<br>Vaccination<br>Records</h2>
    <div class="feature-icon"><svg viewBox="0 0 32 32"><rect x="5" y="5" width="18" height="24" rx="3" fill="#111"/><rect x="10" y="3" width="8" height="5" rx="2" fill="#111" stroke="var(--glow)"/><path d="M9 14h10M9 19h8M9 24h5" stroke="var(--glow)" stroke-width="2"/><path d="M29 14 18 27l-3 1 1-3 11-13z" fill="#111" stroke="var(--glow)"/></svg></div>
    <div class="phone"><div class="screen">
      <div class="island"></div>
      <div class="status"><span>14:35</span><span>●●●</span></div>
      <div class="title">Uploads <small>▦</small></div>
      <div class="upload"><span class="thumb"></span><span><b>Date: 2026-01-28</b><i>Shingles (Herpes Zoster) Velmora</i></span></div>
      <div class="upload"><span class="thumb"></span><span><b>Date: 2026-01-28</b><i>Not linked to a vaccination</i></span></div>
      <div class="upload"><span class="thumb"></span><span><b>Date: 2026-01-28</b><i>Not linked to a vaccination</i></span></div>
      <div class="upload"><span class="thumb"></span><span><b>Date: 2026-01-28</b><i>Not linked to a vaccination</i></span></div>
      <div class="upload"><span class="thumb"></span><span><b>Date: 2026-01-28</b><i>Not linked to a vaccination</i></span></div>
      <div class="upload"><span class="thumb"></span><span><b>Date: 2025-09-25</b><i>Not linked to a vaccination</i></span></div>
      <span class="fab" style="top:206px">+</span>
    </div></div>
  </section>

  <section class="shot" style="left:425px">
    <h2 class="headline">Get Timely<br>Vaccination<br>Reminders</h2>
    <div class="feature-icon"><svg viewBox="0 0 32 32"><rect x="3" y="6" width="22" height="20" rx="3" fill="#111"/><path d="M3 12h22" stroke="var(--glow)" stroke-width="1.5"/><path d="M8 3v6M20 3v6" stroke="#111" stroke-width="2.5"/><path d="M22 16a5 5 0 0 1 5 5v4l2 2H15l2-2v-4a5 5 0 0 1 5-5z" fill="#111" stroke="var(--glow)"/><circle cx="22" cy="29" r="2" fill="#111"/></svg></div>
    <div class="phone"><div class="screen">
      <div class="island"></div>
      <div class="status"><span>14:21</span><span>●●●</span></div>
      <div class="title">My Vaccinations <small>⚙</small></div>
      <div class="tabs"><span class="tab on">Daniel</span><span class="tab">Ruben</span><span class="tab">Noah</span><span class="tab">Ella</span><span class="tab">Mia</span></div>
      <div class="panel">
        <div class="label">Expiring soon <span class="dot"></span></div>
        <div class="row"><span><b>Hepatitis B</b><i>Daniel</i></span><span class="tag">15 days left</span></div>
        <div class="row"><span><b>Corona / Covid-19</b><i>Daniel</i></span><span class="tag">1 month left</span></div>
      </div>
      <div class="panel">
        <div class="row"><span><b>Shingles (Herpes Zoster)</b><i>Brand: Velmora</i><i>Add Date: 2025-11-03</i></span><span class="chev">›</span></div>
        <div class="row"><span><b>Chikungunya</b><i>Last added: 2025-10-17</i><i>Total registrations: 4</i></span><span class="chev">›</span></div>
        <div class="row"><span><b>Meningitis</b><i>Last added: 2025-09-30</i><i>Total registrations: 2</i></span><span class="chev">›</span></div>
        <div class="row"><span><b>MMR (Mumps, Measles, Rubella)</b><i>Last added: 2025-09-17</i><i>Total registrations: 13</i></span><span class="chev">›</span></div>
      </div>
    </div></div>
    <div class="mail"><svg width="38" height="28" viewBox="0 0 38 28"><rect x="1" y="1" width="36" height="26" rx="2" fill="none" stroke="#fff" stroke-width="2.5"/><path d="M2 2l17 14L36 2M2 26l12-12M36 26 24 14" fill="none" stroke="#fff" stroke-width="2.5"/></svg></div>
    <div class="toast"><span class="bell"></span><span><b>Vaccination expired</b><i>The DTP vaccination for your child has expired today,</i><i>please plan a new shot soon.</i></span></div>
  </section>

  <section class="shot" style="left:616px">
    <h2 class="headline">One Overview<br>For The Whole<br>Family</h2>
    <div class="feature-icon"><svg viewBox="0 0 32 32"><path d="M16 9c-2-3-6-1-4 2l4 4 4-4c2-3-2-5-4-2z" fill="#111"/><circle cx="8" cy="12" r="3.5" fill="#111"/><circle cx="24" cy="12" r="3.5" fill="#111"/><circle cx="16" cy="19" r="3" fill="#111"/><path d="M2 29v-7a4 4 0 0 1 4-4h4a4 4 0 0 1 4 4v7zM18 29v-7a4 4 0 0 1 4-4h4a4 4 0 0 1 4 4v7z" fill="#111"/><path d="M11 29v-4a3 3 0 0 1 3-3h4a3 3 0 0 1 3 3v4z" fill="#111" stroke="var(--glow)"/></svg></div>
    <div class="phone"><div class="screen">
      <div class="island"></div>
      <div class="status"><span>14:53</span><span>●●●</span></div>
      <div class="title">Family</div>
      <div class="note">Family members</div>
      <div class="panel">
        <div class="row"><span class="person"><span class="avatar"></span><span><b>Daniel Hart</b><i>You (admin)</i></span></span><span class="chev">›</span></div>
        <div class="row"><span class="person"><span class="avatar"></span><span><b>Noah Hart</b><i>Your child</i></span></span><span class="chev">›</span></div>
        <div class="row"><span class="person"><span class="avatar"></span><span><b>Ella Hart</b><i>Your child</i></span></span><span class="chev">›</span></div>
        <div class="row"><span class="person"><span class="avatar"></span><span><b>Mia Hart</b><i>Your child</i></span></span><span class="chev">›</span></div>
      </div>
      <div class="note">Managed by you</div>
      <div class="panel"><div class="row"><span class="person"><span class="avatar"></span><b>Ruben Vos</b></span></div></div>
      <div class="panel" style="text-align:center;font-size:4.4px;padding:4px">Share</div>
      <div class="note">Add a pet?</div>
      <div class="panel" style="text-align:center;font-size:4.4px;padding:4px">Let us know</div>
      <span class="fab" style="top:211px">+</span>
    </div></div>
  </section>

  <section class="shot" style="left:806px">
    <h2 class="headline">Plan Your<br>Vaccination<br>Directly</h2>
    <div class="feature-icon"><svg viewBox="0 0 32 32"><path d="M21 4l7 7M24 7l-3 3" stroke="#111" stroke-width="2.5"/><path d="M22 9 9 22l-3-3L19 6z" fill="#111"/><path d="M10 16l2 2M13 13l2 2" stroke="var(--glow)" stroke-width="1.2"/><path d="M7 20l-4 8 8-4" stroke="#111" stroke-width="2" fill="none"/></svg></div>
    <div class="phone"><div class="screen">
      <div class="island"></div>
      <div class="status"><span>14:54</span><span>●●●</span></div>
      <div class="title">Hello Daniel <small style="color:var(--red)">●</small></div>
      <div class="segment"><span>Personal Health</span><span class="on">Travel</span></div>
      <div class="panel">
        <div class="label" style="color:var(--blue)">✈ <span>◉</span></div>
        <div style="font-size:5.6px;line-height:6.5px;padding:2px 0">Discover which vaccinations you need for your next trip</div>
        <div style="font-size:3.6px;color:var(--muted)">See which vaccinations you need and where to get them.</div>
        <div class="cta">Start Travel Planner</div>
      </div>
      <div class="panel">
        <div class="label" style="font-size:5.6px;font-weight:500">My Trips</div>
        <div style="font-size:3.6px;color:var(--muted)">Stay updated on your travel vaccinations.</div>
        <div class="row"><span><span class="flag"></span>Sri Lanka</span><i>Departing: Jan 14, 2026</i></div>
        <div class="row"><span><span class="flag"></span>Kenya</span><i>Departing: Dec 17, 2025</i></div>
        <div class="row"><span><b>Travel notification reminders</b><i>You'll get notified about relevant travel alerts.</i></span><span class="toggle"></span></div>
        <div style="font-size:3px;color:var(--muted)">We let you know when new risks or advice appear for your destination.</div>
      </div>
    </div></div>
  </section>

  <section class="shot" style="left:997px">
    <h2 class="headline">Personalised<br>Travel Health<br>Advice</h2>
    <div class="feature-icon"><svg viewBox="0 0 32 32"><path d="M16 28S3 20 3 11a6.5 6.5 0 0 1 13-2 6.5 6.5 0 0 1 13 2c0 9-13 17-13 17z" fill="#111"/><circle cx="16" cy="15" r="5" fill="#fff"/><path d="M16 12v6M13 15h6" stroke="#111" stroke-width="1.8"/></svg></div>
    <div class="phone"><div class="screen">
      <div class="island"></div>
      <div class="status"><span>14:55</span><span>●●●</span></div>
      <div class="title" style="font-size:6.5px">← Plan My Travel Shots</div>
      <div style="margin:0 8px;height:1px;background:var(--line)"><div style="width:25%;height:1px;background:var(--accent)"></div></div>
      <div style="font-size:3.4px;color:var(--muted);padding:3px 8px">Step 1 of 5</div>
      <div class="search">⌕ Where are you traveling next?</div>
      <div class="label" style="padding:2px 8px 4px">Popular destinations</div>
      <div class="grid">
        <div class="dest"><span class="flag"></span>Thailand</div>
        <div class="dest"><span class="flag"></span>India</div>
        <div class="dest"><span class="flag"></span>Indonesia</div>
        <div class="dest"><span class="flag"></span>Brazil</div>
        <div class="dest"><span class="flag"></span>Kenya</div>
        <div class="dest"><span class="flag"></span>South Africa</div>
      </div>
      <div class="more">Show more destinations</div>
    </div></div>
  </section>

</main>
</body>
</html>
```